Verdell Chiropractic, achieve your health goals, get better each day one step at a time

A mobile friendly site, fresh look, easy to navigate, has interface with pw/chirply, etc. Blog posts. Uses new logo. Content and address to current site is mirvaton.com. The current site will give you scope of project for content. The logo is not the final but close. Will upload final next week.
Convey the concept that heath is a process, it does not just happen. We take steps to achieve what we want in life including health.

Target Market(s)

30 to 70 year old. Needing health care

Industry/Entity Type

Health Care

Coding

Coded - Design and coding required

Number of Pages Required

5+ page

Font styles to use
Sans Serif

Colors

Designer to choose colors to be used in the design.

Requirements
Must have
• mobile friendly, easy to navigate, PW/Chirply interface, blog, room for current content
Nice to have
• potential for commerce, statistics
Should not have
• Same old look and feel as everything else out there

```html
<!DOCTYPE html>
<html lang="en">
<head>
<meta charset="utf-8">
<title>Verdell Chiropractic – Better Health Care</title>
<link href="https://fonts.googleapis.com/css2?family=Source+Sans+3:wght@400;600&display=swap" rel="stylesheet">
<style>
:root{
  --canvas:#e1e1e1;
  --teal:#1fbb9b;
  --sky:#5ccaeb;
  --white:#ffffff;
  --ink:#333333;
  --footer:#020202;
  --muted:#777777;
}
*{box-sizing:border-box;margin:0;padding:0}
html,body{width:1200px;height:800px;overflow:hidden;background:var(--canvas);font-family:"Source Sans 3",sans-serif}
.page{position:absolute;left:475px;top:0;width:250px;height:800px;background:var(--white);overflow:hidden}
section,header{position:relative;width:250px}

.topbar{height:10px;background:var(--teal);display:flex;align-items:center;justify-content:flex-end;padding-right:20px;gap:3px}
.topbar .social{width:5px;height:5px;border-radius:50%;background:var(--white)}
.topbar .search{margin-left:6px;width:70px;height:6px;border-bottom:.5px solid var(--white);color:var(--white);font-size:3.5px;line-height:5px}
.nav{height:12px;display:flex;align-items:center;justify-content:space-between;padding:0 20px 0 18px;border-bottom:.5px solid #eee}
.brand{color:var(--teal);font-size:7px;letter-spacing:.2px}
.menu{display:flex;gap:5px;font-size:3.4px;color:var(--teal)}

.hero{height:134px;background:linear-gradient(120deg,#b9bcbd 0%,#8e9599 35%,#5f666a 65%,#3c4247 100%);display:flex;flex-direction:column;align-items:center;justify-content:center;color:var(--white);text-align:center}
.hero h1{font-weight:400;font-size:10px;margin-top:-10px}
.hero p{font-size:4px;margin-top:5px}
.cta-band{height:19px;background:var(--teal);display:flex;align-items:center;justify-content:center}
.btn{background:var(--sky);color:var(--white);font-size:3.6px;padding:2px 6px}

.welcome{height:127px;text-align:center;padding-top:17px}
.heading{color:var(--teal);font-size:6.5px;letter-spacing:.2px}
.welcome .lead{font-size:3.6px;color:var(--ink);width:210px;margin:4px auto 0;line-height:4.4px}
.about{position:absolute;left:24px;top:53px;display:flex;gap:11px;text-align:center}
.about .photo{width:87px;height:59px;background:linear-gradient(135deg,#1b76b8,#4ea9dc 55%,#1a5d95)}
.about .copy{width:108px}
.about .heading{font-size:5.5px}
.about p{font-size:3.5px;color:var(--ink);line-height:4.2px;margin:4px 0 3px}
.about .btn{display:inline-block}

.services{height:91px;background:linear-gradient(100deg,#4b4f52,#7c8285 45%,#5b6064);display:flex;justify-content:space-around;align-items:center;padding:0 6px}
.service{display:flex;flex-direction:column;align-items:center;color:var(--white);font-size:5px;gap:2px;margin-top:-4px}
.service svg{width:20px;height:20px}

.treatment{height:86px;text-align:center;padding-top:12px}
.cards{display:flex;justify-content:center;gap:4px;margin-top:6px}
.card{width:69px;height:45px;background:var(--sky);color:var(--white);font-size:5.5px;display:flex;flex-direction:column;align-items:center;justify-content:center;gap:3px;padding-top:4px}
.card svg{width:11px;height:11px}

.specialists{height:99px;background:linear-gradient(100deg,#6a6e70,#9a9fa2 50%,#6e7376);text-align:center;padding-top:10px;color:var(--white)}
.specialists .heading{color:var(--white);font-size:6px}
.team{display:flex;justify-content:space-around;margin-top:5px;padding:0 8px}
.member{display:flex;flex-direction:column;align-items:center;font-size:4.5px;gap:2px}
.member .portrait{width:52px;height:52px;border-radius:50%;background:linear-gradient(#d8dfe4,#a9b4bb);border:1.5px solid var(--white)}

.contact{height:143px;background:var(--teal);color:var(--white);padding-top:14px}
.contact .heading{color:var(--white);text-align:center;font-size:6.5px}
.details{position:absolute;left:17px;top:35px;font-size:4.4px;line-height:5px}
.details p{margin-bottom:7px}
.details strong{font-weight:600}
.form{position:absolute;left:145px;top:32px;width:88px;display:flex;flex-direction:column;gap:5px}
.field{height:11px;background:var(--white);color:var(--muted);font-size:3.6px;padding:3px 11px}
.field.message{height:23px;padding-top:9px}
.send{width:54px;height:13px;background:var(--sky);color:var(--white);font-size:3.6px;text-align:center;line-height:13px}

.footer{height:79px;background:var(--footer);display:flex;padding:22px 17px 0 18px;gap:0}
.footer .brand{width:56px;font-size:7px}
.col{font-size:3.2px;color:var(--teal);line-height:3.9px}
.col h4{font-weight:400;font-size:4.2px;margin-bottom:4px;margin-top:-4px}
.col.about-us{width:72px;text-align:center;margin-right:18px}
.col.news{width:72px}
</style>
</head>
<body>
<main class="page">
  <header>
    <div class="topbar">
      <span class="social" aria-label="PW"></span>
      <span class="social" aria-label="Chirply"></span>
      <span class="social" aria-label="Network"></span>
      <span class="search">Search</span>
    </div>
    <nav class="nav">
      <span class="brand">Verdell</span>
      <div class="menu"><span>Home</span><span>Meet Doctor</span><span>Testimonials</span><span>FAQS</span><span>Resources</span><span>Contact</span></div>
    </nav>
  </header>

  <section class="hero" role="img" aria-label="Doctor in a white coat showing a tablet to a patient">
    <h1>Better Health Care</h1>
    <p>Lorem Ipsum is simply dummy text of the printing and typesetting</p>
  </section>
  <div class="cta-band"><span class="btn">Make an appointment</span></div>

  <section class="welcome">
    <h2 class="heading">WELCOME TO OUR CLINIC</h2>
    <p class="lead">Lorem Ipsum is simply dummy text of the printing and typesetting industry. Lorem Ipsum has been the industry's standard dummy</p>
    <div class="about">
      <div class="photo" role="img" aria-label="Nurse in blue scrubs holding a stethoscope"></div>
      <div class="copy">
        <h3 class="heading">WHO ARE WE</h3>
        <p>Lorem Ipsum is simply dummy text of the printing and typesetting industry. Lorem Ipsum has been the industry's standard dummy text ever since the 1500s, when an unknown printer took a galley of type and scrambled it to make a type specimen book. It has</p>
        <span class="btn">Read More</span>
      </div>
    </div>
  </section>

  <section class="services" role="img" aria-label="Desk with stethoscope and blood pressure gauge">
    <div class="service"><svg viewBox="0 0 20 20"><circle cx="10" cy="10" r="9.5" fill="#1fbb9b"/><circle cx="10" cy="8" r="3" fill="none" stroke="#fff"/><path d="M5 16c1-3 3-4 5-4s4 1 5 4" fill="none" stroke="#fff"/></svg>Our Stuff</div>
    <div class="service"><svg viewBox="0 0 20 20"><circle cx="10" cy="10" r="9.5" fill="#1fbb9b"/><circle cx="8" cy="8" r="2.5" fill="none" stroke="#fff"/><circle cx="13" cy="9" r="2" fill="none" stroke="#fff"/><path d="M4 15c1-3 6-3 7 0M11 14c1-2 4-2 5 0" fill="none" stroke="#fff"/></svg>Doctors</div>
    <div class="service"><svg viewBox="0 0 20 20"><circle cx="10" cy="10" r="9.5" fill="#1fbb9b"/><rect x="5" y="7" width="10" height="8" fill="none" stroke="#fff"/><path d="M8 7V5h4v2M10 9v4M8 11h4" fill="none" stroke="#fff"/></svg>Health Care</div>
    <div class="service"><svg viewBox="0 0 20 20"><circle cx="10" cy="10" r="9.5" fill="#1fbb9b"/><path d="M5 15V8h4v7M9 15V5h6v10M4 15h12M11 7h2M11 10h2" fill="none" stroke="#fff"/></svg>Branches</div>
  </section>

  <section class="treatment">
    <h2 class="heading">TREATMENT</h2>
    <div class="cards">
      <div class="card"><svg viewBox="0 0 12 12"><circle cx="6" cy="4" r="2.5" fill="none" stroke="#fff"/><path d="M1.5 11.5c0-3 2-4 4.5-4s4.5 1 4.5 4z" fill="none" stroke="#fff"/></svg>Headaches</div>
      <div class="card"><svg viewBox="0 0 12 12"><path d="M2 3c2-2 6-2 8 0l-1 3v5H3V6z" fill="none" stroke="#fff"/></svg>Neck Pain</div>
      <div class="card"><svg viewBox="0 0 12 12"><circle cx="6" cy="1.8" r="1.3" fill="#fff"/><path d="M6 4v3l-2 4M6 7l3 1v3" fill="none" stroke="#fff" stroke-width="1.2"/></svg>Knee Pain</div>
    </div>
  </section>

  <section class="specialists" role="img" aria-label="Clinic treatment room">
    <h2 class="heading">OUR SPECIALIST</h2>
    <div class="team">
      <div class="member"><div class="portrait" role="img" aria-label="Portrait of senior doctor"></div>Loreum Ipsum</div>
      <div class="member"><div class="portrait" role="img" aria-label="Portrait of doctor" style="background:linear-gradient(#a6d7ef,#4a9fcf)"></div>Loreum Ipsum</div>
      <div class="member"><div class="portrait" role="img" aria-label="Portrait of surgeon" style="background:linear-gradient(#e6eef4,#9fb7d8)"></div>Loreum Ipsum</div>
    </div>
  </section>

  <section class="contact">
    <h2 class="heading">CONTACT</h2>
    <div class="details">
      <p><strong>Marla Venn DC PA</strong><br><br>4870 Larkspur Road West<br><br>Brenton, TX 70412</p>
      <p>555.014.2200 Off</p>
      <p>555.014.2210 Fax</p>
    </div>
    <div class="form">
      <div class="field">Name</div>
      <div class="field">Email</div>
      <div class="field">Subject</div>
      <div class="field message">Message</div>
      <div class="send">Send</div>
    </div>
  </section>

  <footer class="footer">
    <span class="brand">Verdell</span>
    <div class="col about-us">
      <h4>About us</h4>
      <p>Lorem Ipsum is simply dummy text of the printing and typesetting industry. Lorem Ipsum has been the industry's standard dummy text ever since the 1500s, when an unknown printer took a galley of type and scrambled it to make a type specimen book. It has</p>
    </div>
    <div class="col news">
      <h4>Latest News</h4>
      <p>Lorem Ipsum is simply dummy text of</p>
      <p>Lorem Ipsum is simply dummy text of</p>
      <p>Lorem Ipsum is simply dummy text of</p>
      <p>Lorem Ipsum is simply dummy text of</p>
    </div>
  </footer>
</main>
</body>
</html>
```